Postcard Design

business name: COZY HOUR KEEPER. I am a mother of 2 well adjusted, successful teenage boys. I decided to start this company caring for kids who are home sick, unable to go to daycare or school, and when their parent cant stay home with them. I was also a career woman for many years, with no friends available or family nearby to help when i was in an emergency situation for childcare. I know how stressful it can be when a child gets sick suddenly and unexpectedly. I would like to help out those parents in need, that have pressing schedules and a sick child at home that they really want to take care of, but cant due to their work pressures and priorities. I want parents to know that their child is safe and I can help them when in need, at last minute. The design should show the child is safe and well cared for and the parent is at ease, able to accomplish their obligations. I have also founded a nonprofit environmental education program in which I teach children in youth summer camps. I have taught creativity arts combined with science curriculum in kindergarten to 8th grade non-formal teaching for the past 5 years. This is a small community, and many people know me. I will be handing out these postcards to local daycares and people I know.

Industry/Entity Type

Business

```html
<!DOCTYPE html>
<html lang="en">
<head>
<meta charset="utf-8">
<title>Cozy Hour Keeper – Postcard</title>
<link rel="stylesheet" href="https://fonts.googleapis.com/css2?family=Archivo+Black&family=Lato:wght@400;700&family=Oswald:wght@500;600&family=Roboto+Condensed:wght@700&family=Roboto:ital,wght@1,400&display=swap">
<style>
:root{
  --bg:#8a8a8a;
  --blue:#2e4fa6;
  --blue-dark:#233f8c;
  --orange:#f7931e;
  --orange-light:#fbb54a;
  --yellow:#f7e51c;
  --pink:#e6358d;
  --green:#8cc63f;
  --ink:#222222;
  --white:#ffffff;
  --photo-a:#e8d7c0;
  --photo-b:#b89270;
}
*{box-sizing:border-box;margin:0;padding:0}
html,body{width:900px;height:1200px;overflow:hidden}
body{background:var(--bg);position:relative;font-family:"Lato",sans-serif}
.card{position:absolute;left:143px;width:615px;overflow:hidden;background:var(--white);box-shadow:0 3px 8px rgba(0,0,0,.35)}
.card--front{top:97px;height:475px}
.card--back{top:628px;height:476px}
.card__shapes{position:absolute;inset:0;width:100%;height:100%}
.abs{position:absolute}

/* front */
.experience{left:22px;top:22px;font-family:"Archivo Black",sans-serif;line-height:1}
.experience__years{color:var(--yellow);font-size:19px;letter-spacing:.5px}
.experience__label{color:var(--white);font-family:"Lato",sans-serif;font-weight:700;font-size:16px;margin-top:5px}
.headline{left:21px;top:128px;line-height:1}
.headline__top{font-family:"Roboto Condensed",sans-serif;font-weight:700;font-size:42px;color:var(--ink);letter-spacing:.5px}
.headline__bottom{font-family:"Roboto",sans-serif;font-style:italic;font-size:42px;color:var(--white);margin-top:6px}
.intro{left:22px;top:243px;width:226px;font-size:12.5px;line-height:16.2px;color:var(--ink);text-align:justify}
.hero-photo{left:277px;top:-66px;width:340px;height:340px;border-radius:50%;
  background:radial-gradient(circle at 45% 60%,var(--photo-a),var(--photo-b));
  box-shadow:0 0 0 5px var(--green),0 0 0 9px var(--yellow),0 0 0 15px var(--pink)}
.badge{left:405px;top:243px;width:144px;height:136px}
.badge__text{position:absolute;inset:0;display:flex;align-items:center;justify-content:center;text-align:center;
  font-family:"Archivo Black",sans-serif;font-size:17px;line-height:23px;color:var(--ink)}
.contact-bar{left:0;top:428px;width:615px;display:flex;align-items:center;color:var(--white);font-weight:700}
.contact-bar__name{margin-left:25px;font-size:17px}
.contact-bar__phone{margin-left:22px;font-size:18px}
.contact-bar__web{margin-left:18px;font-size:15px;display:flex;align-items:center;gap:6px}
.globe{width:10px;height:10px}

/* back */
.portrait{left:19px;top:38px;width:94px;height:94px;border-radius:50%;
  background:linear-gradient(160deg,#dfe3e8,#8f9bb0);box-shadow:0 0 0 4px var(--blue),0 0 0 6px var(--white)}
.name-pill{left:123px;top:69px;width:116px;height:48px;border-radius:0 24px 24px 0;
  background:linear-gradient(90deg,var(--green),var(--yellow));display:flex;align-items:center;justify-content:center;
  font-weight:700;font-size:13px;color:var(--ink)}
.about{left:21px;top:170px;width:253px;font-size:12.5px;line-height:16.3px;color:var(--ink);text-align:justify}
.cta{left:21px;top:318px;line-height:1}
.cta__line1{font-family:"Oswald",sans-serif;font-weight:500;font-size:17px;color:var(--white)}
.cta__line2{font-family:"Archivo Black",sans-serif;font-size:15px;color:#000;margin-top:7px}
.cta__line3{display:flex;align-items:baseline;gap:10px;margin-top:6px}
.cta__call{font-family:"Oswald",sans-serif;font-weight:600;font-size:26px;color:var(--white)}
.cta__phone{font-family:"Archivo Black",sans-serif;font-size:15px;color:var(--ink)}
.footer{left:20px;top:422px;color:var(--white);font-size:13px;line-height:19px}
.footer__web{display:flex;align-items:center;gap:5px}
.stamp-box{left:525px;top:33px;width:55px;height:75px;border:1.5px solid #555}
</style>
</head>
<body>

<section class="card card--front">
  <svg class="card__shapes" viewBox="0 0 615 475" aria-hidden="true">
    <defs>
      <radialGradient id="sunOrange" cx="0.3" cy="0.55" r="0.75">
        <stop offset="0" stop-color="#fcc45a"/>
        <stop offset="0.6" stop-color="#f8a12c"/>
        <stop offset="1" stop-color="#f4861a"/>
      </radialGradient>
    </defs>
    <rect width="615" height="475" fill="url(#sunOrange)"/>
    <path d="M0 0 H285 C240 55 130 80 0 92 Z" fill="var(--blue)"/>
    <path d="M0 97 C130 85 240 60 290 4" fill="none" stroke="var(--pink)" stroke-width="4"/>
    <path d="M0 104 C135 92 245 66 296 8" fill="none" stroke="var(--green)" stroke-width="5"/>
    <path d="M0 412 C200 370 420 372 615 402 V475 H0 Z" fill="var(--blue)"/>
    <path d="M0 400 C200 358 420 360 615 390" fill="none" stroke="var(--green)" stroke-width="5"/>
    <path d="M0 392 C200 350 420 352 615 382" fill="none" stroke="var(--pink)" stroke-width="4"/>
  </svg>

  <div class="abs hero-photo" role="img" aria-label="Photo: a caregiver comforting a sick child resting in bed"></div>

  <div class="abs experience">
    <div class="experience__years">OVER 14 YEARS</div>
    <div class="experience__label">CHILD CARE EXPERIENCE</div>
  </div>

  <h1 class="abs headline">
    <div class="headline__top">COZY HOUR</div>
    <div class="headline__bottom">KEEPER</div>
  </h1>

  <p class="abs intro">I would like to help out those parents in need who have pressing schedules and a sick child at home. I can bring relief to stressed parents who really want to stay home to take care of their child, but cant due to their work obligations and priorities.</p>

  <div class="abs badge">
    <svg width="144" height="136" viewBox="0 0 144 136" aria-hidden="true">
      <g fill="var(--white)">
        <circle cx="72" cy="68" r="64"/>
      </g>
      <g fill="var(--green)">
        <circle cx="72" cy="68" r="52"/>
        <circle cx="72" cy="16" r="14"/><circle cx="98" cy="23" r="14"/><circle cx="117" cy="42" r="14"/>
        <circle cx="124" cy="68" r="14"/><circle cx="117" cy="94" r="14"/><circle cx="98" cy="113" r="14"/>
        <circle cx="72" cy="120" r="14"/><circle cx="46" cy="113" r="14"/><circle cx="27" cy="94" r="14"/>
        <circle cx="20" cy="68" r="14"/><circle cx="27" cy="42" r="14"/><circle cx="46" cy="23" r="14"/>
      </g>
    </svg>
    <div class="badge__text">But you<br>must go<br>to work<br>today</div>
  </div>

  <div class="abs contact-bar">
    <span class="contact-bar__name">Mara Lindqvist</span>
    <span class="contact-bar__phone">(206) 555-0147</span>
    <span class="contact-bar__web">
      <svg class="globe" viewBox="0 0 10 10" aria-hidden="true"><circle cx="5" cy="5" r="4.3" fill="none" stroke="var(--orange)" stroke-width="1.2"/><path d="M0.7 5H9.3M5 0.7V9.3" stroke="var(--orange)" stroke-width="1"/></svg>
      www.carefinder.example/maral482/cc
    </span>
  </div>
</section>

<section class="card card--back">
  <svg class="card__shapes" viewBox="0 0 615 476" aria-hidden="true">
    <defs>
      <radialGradient id="backOrange" cx="0.2" cy="0.3" r="0.9">
        <stop offset="0" stop-color="#fbb54a"/>
        <stop offset="1" stop-color="#f4861a"/>
      </radialGradient>
    </defs>
    <path d="M0 0 H311 C333 150 323 300 287 412 H0 Z" fill="var(--green)"/>
    <path d="M0 0 H304 C326 150 316 300 281 412 H0 Z" fill="var(--blue)"/>
    <path d="M0 0 H295 C317 150 307 300 272 412 H0 Z" fill="url(#backOrange)"/>
    <rect x="0" y="410" width="290" height="66" fill="var(--blue)"/>
  </svg>

  <div class="abs portrait" role="img" aria-label="Portrait photo of the caregiver"></div>
  <div class="abs name-pill">Mara Lindqvist</div>

  <p class="abs about">I am a 10-year resident, Cedar Harbor Island mom, who would like to help parents in need. As an Island parent, I have been there, and know how logistics and illness can cause stressful situations. You can count on me when your child gets sick and you need a backup. I can also work as a fill-in when your nanny is sick.</p>

  <div class="abs cta">
    <div class="cta__line1">For your last minute request</div>
    <div class="cta__line2">Or advanced scheduling</div>
    <div class="cta__line3"><span class="cta__call">Call Mara at</span><span class="cta__phone">(206) 555-0147</span></div>
  </div>

  <div class="abs footer">
    <div>Mara Lindqvist</div>
    <div class="footer__web">
      <svg class="globe" viewBox="0 0 10 10" aria-hidden="true"><circle cx="5" cy="5" r="4.3" fill="none" stroke="var(--orange)" stroke-width="1.2"/><path d="M0.7 5H9.3M5 0.7V9.3" stroke="var(--orange)" stroke-width="1"/></svg>
      www.carefinder.example/maral482/cc
    </div>
  </div>

  <div class="abs stamp-box"></div>
</section>

</body>
</html>
```